Velmora Interiors Stationary Set

Velmora Interiors is a bespoke interior design firm set to provide services to VIP clients with elegance and minimalism is the main theme for our stationary set. We require a full stationary set covering A4 letterhead, A4 & A3 envelopes, business cards, USB's, CDs, email signature and any other item the designer sees fit. logo is already designed and finalized, and we require the designer to use it as is without modifying the logo.

Address to be used on letterhead / business cards ...etc shall be as follows:

Phone : +971 2 518 3074
P.O. Box : 609318
Address: Block C&D, Bldg. 27, Court 14, Abu Dhabi, United Arab Emirates
Website: www.velmorainteriors-example.com

Target Market(s)

VIP Clients

Industry/Entity Type

Interior Design

Other font styles liked:
• something to be unique

Colors

Designer to choose colors to be used in the design.

Requirements
Must have
• Elegant, minimalistic
Nice to have
• Simple yet elegant design having a sharp yet clean cut format
Should not have
• No additional colours, just colours that are used in the logo (silver, black or gold)

```html
<!DOCTYPE html>
<html lang="en">
<head>
<meta charset="utf-8">
<title>Velmora Interiors Stationery Set</title>
<link href="https://fonts.googleapis.com/css2?family=Lato:wght@400;700&family=Roboto:wght@400;500&display=swap" rel="stylesheet">
<style>
:root{
  --gold:#b0955a;
  --gold-dark:#9c8249;
  --charcoal:#58585a;
  --ink:#2b2b2b;
  --text:#555555;
  --paper:#ffffff;
  --paper-soft:#f4f4f4;
  --backdrop:#e9e6e1;
}
*{box-sizing:border-box;margin:0;padding:0}
html,body{width:1200px;height:945px;overflow:hidden}
body{background:var(--backdrop);font-family:"Lato",sans-serif;color:var(--text);position:relative}
.sheet{position:absolute;background:linear-gradient(135deg,var(--paper),var(--paper-soft));box-shadow:0 2px 8px rgba(0,0,0,.12);overflow:hidden}
.band{position:absolute;left:0;bottom:0;width:100%;display:block}
.brand-name{font-family:"Lato",sans-serif;font-weight:400;color:var(--gold);letter-spacing:.18em;text-transform:uppercase;white-space:nowrap}
.brand-name.light{color:var(--paper)}
.contact-list{list-style:none}
.contact-list li{display:flex;align-items:center;gap:5px;white-space:nowrap}
.contact-list svg{flex:none;fill:none;stroke:var(--gold);stroke-width:1.6}

/* letterhead */
.letterhead{left:40px;top:40px;width:470px;height:665px}
.letterhead .brand-name{position:absolute;left:38px;top:48px;font-size:15px}
.letterhead .contact{position:absolute;left:312px;top:38px;border-left:2px solid var(--gold);padding-left:12px;font-size:7.6px;color:var(--ink);line-height:1.5}
.letterhead .contact svg{width:7px;height:7px}
.letter{position:absolute;left:50px;top:136px;width:372px;font-size:7.2px;line-height:1.42;color:var(--text)}
.letter .date{margin-bottom:12px}
.letter .recipient{margin-bottom:22px}
.letter .recipient strong{color:var(--ink);font-weight:700}
.letter p{margin-bottom:11px;text-align:justify}
.letter .salutation{margin-bottom:9px}
.letter .closing{margin-top:26px;margin-bottom:6px}
.signature{width:150px;height:16px;background:linear-gradient(90deg,rgba(43,43,43,.35),rgba(43,43,43,.12));border-radius:8px}
.letterhead .footer-address{position:absolute;left:0;right:0;bottom:26px;text-align:center;font-size:7.6px;color:var(--ink)}

/* envelope front */
.envelope-front{left:580px;top:40px;width:580px;height:268px}
.envelope-front .brand-name{position:absolute;right:34px;top:54px;font-size:15px}
.envelope-front .contact{position:absolute;left:28px;top:158px;font-size:7.4px;color:var(--ink);line-height:1.45}
.envelope-front .contact svg{width:7px;height:7px}
.envelope-front .address{position:absolute;left:28px;top:210px;font-size:7.2px;color:var(--ink);line-height:1.45}

/* envelope back */
.envelope-back{left:580px;top:328px;width:580px;height:268px;background:var(--paper)}
.envelope-back svg.flap{position:absolute;left:0;top:0;width:100%;height:100%}
.envelope-back .brand-name{position:absolute;left:0;right:0;top:52px;text-align:center;font-size:15px}

/* business cards */
.card{width:280px;height:162px;border-radius:10px;top:620px}
.card-front{left:580px}
.card-back{left:880px;background:linear-gradient(135deg,#b89e63,var(--gold-dark))}
.card-front .brand-name{position:absolute;left:18px;width:108px;top:56px;font-size:11px;line-height:1.5;text-align:center;white-space:normal}
.card-front .brand-name span{display:block}
.card-front .divider{position:absolute;left:140px;top:46px;width:2px;height:54px;background:var(--gold)}
.card-front .person{position:absolute;left:152px;top:46px;font-family:"Roboto",sans-serif}
.card-front .person .name{font-size:8.5px;font-weight:500;color:var(--gold)}
.card-front .person .role{font-size:6px;color:var(--ink);margin-bottom:9px}
.card-front .contact{font-family:"Roboto",sans-serif;font-size:6px;color:var(--ink);line-height:1.45}
.card-front .contact svg{width:6px;height:6px}
.card-front .card-address{position:absolute;left:0;right:0;top:130px;text-align:center;font-family:"Roboto",sans-serif;font-size:5.6px;color:var(--ink)}
.card-back .brand-name{position:absolute;left:0;right:0;top:70px;text-align:center;font-size:15px}
.card-back .web{position:absolute;left:0;right:0;top:136px;text-align:center;font-family:"Roboto",sans-serif;font-size:6px;color:var(--paper)}
</style>
</head>
<body>

<svg width="0" height="0" style="position:absolute" aria-hidden="true">
  <defs>
    <symbol id="icon-phone" viewBox="0 0 10 10"><path d="M2 1l2 2-1 1.2a6 6 0 0 0 2.8 2.8L7 6l2 2-1.3 1.2C4.5 9 1 5.5.8 2.3z"/></symbol>
    <symbol id="icon-mail" viewBox="0 0 10 10"><rect x="1" y="2.2" width="8" height="5.6"/><path d="M1 2.4l4 3 4-3"/></symbol>
    <symbol id="icon-web" viewBox="0 0 10 10"><circle cx="5" cy="5" r="4"/><path d="M1 5h8M5 1c2 2.2 2 5.8 0 8M5 1c-2 2.2-2 5.8 0 8"/></symbol>
  </defs>
</svg>

<section class="sheet letterhead" aria-label="Letterhead">
  <div class="brand-name">Velmora Interiors</div>
  <ul class="contact contact-list">
    <li><svg><use href="#icon-phone"/></svg>+971 2 518 3074</li>
    <li><svg><use href="#icon-mail"/></svg>info@velmorainteriors-example.com</li>
    <li><svg><use href="#icon-web"/></svg>www.velmorainteriors-example.com</li>
  </ul>
  <div class="letter">
    <div class="date">01 January 2050</div>
    <div class="recipient"><strong>Company (Pvt) Ltd.</strong><br>PO Box 3355 Mainville St<br>Sample City Country 3355</div>
    <div class="salutation">Dear Daniel Marsh,</div>
    <p>Lorem ipsum dolor sit amet, consectetuer adipiscing elit, sed diam nonummy nibh euismod tincidunt ut laoreet dolore magna aliquam erat volutpat. Ut wisi enim ad minim veniam, quis nostrud exerci tation ullamcorper suscipit lobortis nisl ut aliquip ex ea commodo consequat. Duis dolore te feugait nulla facilisi. Nam liber tempor cum soluta nobis eleifend option congue nihil imperdiet doming id quod mazim placerat facer possim assum. Lorem ipsum dolor sit amet, consectetuer adipiscing elit, sed diam nonummy nibh euismod tincidunt ut laoreet dolore magna aliquam erat volutpat. Ut wisi enim ad minim veniam, quis nostrud exerci tation ullamcorper suscipit lobortis nisl ut aliquip ex ea commodo consequat.</p>
    <p>Consectetuer adipiscing elit, sed diam nonummy nibh euismod tincidunt ut laoreet dolore magna aliquam erat volutpat. Ut wisi enim ad minim veniam, quis nostrud exerci tation ullamcorper suscipit lobortis nisl ut aliquip ex ea commodo consequat. Consectetuer adipiscing elit, sed diam nonummy nibh euismod tincidunt ut laoreet dolore magna aliquam erat volutpat. Ut wisi enim ad minim veniam, quis nostrud exerci tation ullamcorper suscipit lobortis nisl ut aliquip ex ea commodo consequat.</p>
    <p>Consectetuer adipiscing elit, sed diam nonummy nibh euismod tincidunt ut laoreet dolore magna aliquam erat volutpat. Ut wisi enim ad minim veniam, quis nostrud exerci tation ullamcorper suscipit lobortis nisl ut aliquip ex ea commodo consequat. Consectetuer adipiscing elit, sed diam nonummy nibh euismod tincidunt ut laoreet dolore magna aliquam erat volutpat. Ut wisi enim ad minim veniam, quis nostrud exerci tation ullamcorper suscipit lobortis nisl ut aliquip ex ea commodo consequat.</p>
    <div class="closing">Sincerely Yours</div>
    <div class="signature" role="img" aria-label="Handwritten signature of Owen Carter Hale"></div>
  </div>
  <div class="footer-address">P.O. Box : 609318, Block C&amp;D, Bldg. 27, Court 14, Abu Dhabi, UAE</div>
  <svg class="band" viewBox="0 0 470 8" preserveAspectRatio="none" height="8"><polygon points="0,0 236,0 230,8 0,8" fill="var(--gold)"/><polygon points="240,0 470,0 470,8 234,8" fill="var(--charcoal)"/></svg>
</section>

<section class="sheet envelope-front" aria-label="Envelope front">
  <div class="brand-name">Velmora Interiors</div>
  <ul class="contact contact-list">
    <li><svg><use href="#icon-phone"/></svg>+971 2 518 3074</li>
    <li><svg><use href="#icon-mail"/></svg>info@velmorainteriors-example.com</li>
    <li><svg><use href="#icon-web"/></svg>www.velmorainteriors-example.com</li>
  </ul>
  <div class="address">P.O. Box : 609318, Block C&amp;D, Bldg. 27<br>Court 14, Abu Dhabi, UAE</div>
  <svg class="band" viewBox="0 0 580 8" preserveAspectRatio="none" height="8"><polygon points="0,0 290,0 284,8 0,8" fill="var(--gold)"/><polygon points="294,0 580,0 580,8 288,8" fill="var(--charcoal)"/></svg>
</section>

<section class="sheet envelope-back" aria-label="Envelope back">
  <svg class="flap" viewBox="0 0 580 268" preserveAspectRatio="none" aria-hidden="true">
    <polyline points="0,268 290,120 580,268" fill="none" stroke="#e2e2e2" stroke-width="1"/>
    <path d="M0,0 H580 V64 Q580,104 540,108 H40 Q0,104 0,64 Z" fill="var(--gold)"/>
  </svg>
  <div class="brand-name light">Velmora Interiors</div>
</section>

<section class="sheet card card-front" aria-label="Business card front">
  <div class="brand-name"><span>Velmora</span><span>Interiors</span></div>
  <div class="divider"></div>
  <div class="person">
    <div class="name">Adam Kerrow</div>
    <div class="role">Managing Director</div>
    <ul class="contact contact-list">
      <li><svg><use href="#icon-phone"/></svg>+971 2 518 3074</li>
      <li><svg><use href="#icon-mail"/></svg>info@velmorainteriors-example.com</li>
      <li><svg><use href="#icon-web"/></svg>www.velmorainteriors-example.com</li>
    </ul>
  </div>
  <div class="card-address">P.O. Box : 609318, Block C&amp;D, Bldg. 27, Court 14, Abu Dhabi, UAE</div>
  <svg class="band" viewBox="0 0 280 6" preserveAspectRatio="none" height="6"><polygon points="0,0 168,0 163,6 0,6" fill="var(--gold)"/><polygon points="171,0 280,0 280,6 166,6" fill="var(--charcoal)"/></svg>
</section>

<section class="sheet card card-back" aria-label="Business card back">
  <div class="brand-name light">Velmora Interiors</div>
  <div class="web">www.velmorainteriors-example.com</div>
</section>

</body>
</html>
```